Letterhead

Can you please design me a letterhead that I can use electronically in word as a template. I have attached my business card as I would like the design to reflect this logo.

```html
<!DOCTYPE html>
<html lang="en">
<head>
<meta charset="utf-8">
<title>Marlowe Business Consultants – Letterhead</title>
<link href="https://fonts.googleapis.com/css2?family=Open+Sans:wght@400;600;700&display=swap" rel="stylesheet">
<style>
  :root {
    --brand-red: #b61f29;
    --brand-maroon: #5a0000;
    --ink: #3a3a3a;
    --ghost: #ececec;
    --ghost-sub: #c9c9c9;
    --paper: #ffffff;
  }
  * { margin: 0; padding: 0; box-sizing: border-box; }
  html, body { width: 843px; height: 1200px; overflow: hidden; background: var(--paper); }
  body { font-family: "Open Sans", Arial, sans-serif; color: var(--ink); }

  .letterhead { position: relative; width: 843px; height: 1200px; overflow: hidden; }

  .header-band { position: absolute; top: 0; left: 0; width: 843px; height: 76px; }

  .ghost-brand { position: absolute; left: 46px; top: 26px; }
  .ghost-brand__name {
    font-size: 66px; font-weight: 400; line-height: 1; color: var(--ghost); letter-spacing: 1px;
  }
  .ghost-brand__tagline {
    font-size: 16px; color: var(--ghost-sub); margin-top: 6px; margin-left: 4px;
  }

  .header-brand { position: absolute; right: 34px; top: 14px; text-align: center; }
  .header-brand__name {
    font-size: 38px; font-weight: 400; line-height: 1; color: var(--paper); letter-spacing: 1px;
  }
  .header-brand__tagline {
    font-size: 9px; font-weight: 600; color: #2a0a0a; margin-top: 3px;
  }

  .side-brand__name,
  .side-brand__tagline {
    position: absolute; white-space: nowrap; line-height: 1;
    transform-origin: left top; transform: rotate(-90deg);
  }
  .side-brand__name { left: 706px; top: 1172px; font-size: 76px; color: var(--ghost); letter-spacing: 1px; }
  .side-brand__tagline { left: 798px; top: 1168px; font-size: 18px; color: var(--ghost-sub); }

  .footer-contact { position: absolute; left: 58px; top: 1144px; }
  .footer-contact__name { font-size: 13px; font-weight: 700; color: #444; }
  .footer-contact__role { font-size: 12px; font-weight: 400; color: var(--brand-red); }
  .footer-contact__details { font-size: 10.5px; margin-top: 3px; color: #333; }
  .label { color: var(--brand-red); }
  .divider { color: var(--brand-red); font-weight: 700; padding: 0 3px; }

  .footer-band { position: absolute; left: 0; bottom: 0; width: 843px; height: 14px; background: var(--brand-red); }
</style>
</head>
<body>
<div class="letterhead">
  <svg class="header-band" viewBox="0 0 843 76" aria-hidden="true">
    <polygon points="28,0 268,0 478,76" fill="var(--brand-maroon)"/>
    <polygon points="268,0 843,0 843,76 478,76" fill="var(--brand-red)"/>
  </svg>

  <div class="ghost-brand">
    <div class="ghost-brand__name">marlowe</div>
    <div class="ghost-brand__tagline">Business Consultants Pty Ltd</div>
  </div>

  <div class="header-brand">
    <div class="header-brand__name">marlowe</div>
    <div class="header-brand__tagline">Business Consultants Pty Ltd</div>
  </div>

  <div class="side-brand">
    <div class="side-brand__name">marlowe</div>
    <div class="side-brand__tagline">Business Consultants Pty Ltd</div>
  </div>

  <div class="footer-contact">
    <div><span class="footer-contact__name">Helena Marsh</span><span class="divider">|</span><span class="footer-contact__role">Principal</span></div>
    <div class="footer-contact__details">
      <span class="label">P</span> : 0400 518 372<span class="divider">|</span><span class="label">E</span> : helena@marlowe.net.au<span class="divider">|</span><span class="label">ACN</span> : 061 284 935
    </div>
  </div>

  <div class="footer-band"></div>
</div>
</body>
</html>
```